Now We Rise stop Smoking

Hi Iam looking for a Cover for a CD/DVD wich will also be used online on our website. The title of which is "Now We Rise Stop smoking for good" I have included a file with the website LOGO which can be included on the cover if you see fit. The method that we are using is unique and has not been done before also in trials it has had an almost 100% success rate. The sites main colours will be white blue and green. As I have said the site is "Now We Rise" and we will be launching a number of titles all beginning "Now We Rise" i.e.. "Now We Rise stop smoking for good" "Now we rise beat depression" "Now we rise conquer gambling" etc. It needs to be concise clean and also getting the message across, i.e that this method works and works well.

```html
<!DOCTYPE html>
<html lang="en">
<head>
<meta charset="utf-8">
<title>Now We Rise – Stop Smoking for Good</title>
<link rel="stylesheet" href="https://fonts.googleapis.com/css2?family=Anton&display=swap">
<style>
  :root {
    --page-bg: #ffffff;
    --green-deep: #4c9416;
    --green-mid: #8fcf16;
    --green-lime: #c3ee2c;
    --green-haze: #f2fadc;
    --title-green: #4a9d1f;
    --title-green-dark: #2f7a12;
    --sign-red: #d8221c;
    --cig-white: #f4f4f4;
    --cig-filter: #e08a2e;
    --brand-grey: #4a4a4a;
    --brand-dot: #5aa81e;
  }
  * { margin: 0; padding: 0; box-sizing: border-box; }
  html, body {
    width: 1200px;
    height: 960px;
    overflow: hidden;
    background: var(--page-bg);
  }
  .canvas {
    position: relative;
    width: 1200px;
    height: 960px;
  }
  .cover {
    position: absolute;
    left: 280px;
    top: 30px;
    width: 640px;
    height: 900px;
    background: linear-gradient(180deg,
      var(--green-deep) 0%,
      var(--green-mid) 22%,
      var(--green-lime) 34%,
      var(--green-haze) 48%,
      #ffffff 60%,
      #ffffff 100%);
    font-family: "Anton", "Arial Narrow", sans-serif;
    text-align: center;
  }
  .cover-title {
    position: absolute;
    left: 0;
    right: 0;
    top: 340px;
    font-weight: 400;
    font-size: 88px;
    line-height: 112px;
    letter-spacing: 2px;
    text-transform: uppercase;
    color: var(--title-green);
    text-shadow: 0 2px 0 var(--title-green-dark), 0 4px 8px rgba(40, 90, 10, 0.25);
  }
  .cover-title .line { display: block; }
  .no-smoking-sign {
    display: inline-block;
    width: 76px;
    height: 76px;
    vertical-align: -4px;
    margin: 0 2px;
  }
  .brand {
    position: absolute;
    left: 0;
    right: 0;
    top: 790px;
    display: flex;
    align-items: center;
    justify-content: center;
    gap: 12px;
  }
  .brand-dot {
    width: 52px;
    height: 52px;
    border-radius: 50%;
    background: var(--brand-dot);
  }
  .brand-name {
    font-family: "Anton", "Arial Narrow", sans-serif;
    font-size: 36px;
    color: var(--brand-grey);
  }
</style>
</head>
<body>
  <main class="canvas">
    <section class="cover">
      <h1 class="cover-title">
        <span class="line">Now We Rise</span>
        <span class="line">Stop Sm<svg class="no-smoking-sign" viewBox="0 0 100 100" role="img" aria-label="O">
            <g transform="rotate(-52 50 50)">
              <rect x="12" y="43" width="76" height="14" fill="var(--cig-white)" stroke="#bbbbbb" stroke-width="1.5"/>
              <rect x="12" y="43" width="20" height="14" fill="var(--cig-filter)"/>
            </g>
            <circle cx="50" cy="50" r="42" fill="none" stroke="var(--sign-red)" stroke-width="12"/>
            <line x1="22" y1="22" x2="78" y2="78" stroke="var(--sign-red)" stroke-width="12"/>
          </svg>king</span>
        <span class="line">For Good</span>
      </h1>
      <div class="brand">
        <span class="brand-dot"></span>
        <span class="brand-name">Now we rise</span>
      </div>
    </section>
  </main>
</body>
</html>
```